upmarket Hair salon A5 flyer design colour double sided

Phone number 9318 7061
address is shop 3/7 Marlowe pde Butler
Hi i am wanting a flyer that is upmarket and elegant for my hair salon Velvet Strands For Hair if any pics of hair must look great.
both side must have logo and contact details on
offer side 1
50% off
style cut and finish
*not valid Saturdays
*expires 31/03/15
*butler salon only
*not valid with any other offers
offer side 2
1/2 head foils or all over colour,
cut and finish
$120
*toners and treatment extra costs
*expires 31/03/15
*butler salon only

```html
<!DOCTYPE html>
<html lang="en">
<head>
<meta charset="utf-8">
<title>Velvet Strands For Hair – A5 Flyer</title>
<link rel="stylesheet" href="https://fonts.googleapis.com/css2?family=Share+Tech+Mono&family=Questrial&family=Hind:wght@400&display=swap">
<style>
  :root {
    --teal-deep: #1f8a8c;
    --teal: #3a9ea0;
    --glow: #ffffff;
    --ink: #1a1a1a;
    --paper: #ffffff;
    --rule: rgba(255,255,255,0.55);
  }
  * { margin: 0; padding: 0; box-sizing: border-box; }
  html, body {
    width: 1200px; height: 816px; overflow: hidden;
    background: var(--paper);
  }
  .canvas { position: relative; width: 1200px; height: 816px; }

  .flyer {
    position: absolute; top: 18px; width: 565px; height: 770px;
    overflow: hidden;
    box-shadow: 4px 5px 6px rgba(0,0,0,0.55);
    color: var(--paper);
  }
  .flyer--colour { left: 28px;
    background:
      radial-gradient(circle at 50% 72%, var(--glow) 0, rgba(255,255,255,0.85) 70px, rgba(255,255,255,0) 230px),
      radial-gradient(ellipse 300px 330px at 50% 50%, rgba(255,255,255,0.9) 0, rgba(190,230,230,0.6) 120px, rgba(58,158,160,0) 330px),
      var(--teal);
  }
  .flyer--cut { left: 605px; background: var(--teal-deep); }

  .hero-photo {
    position: absolute; inset: 0;
    background:
      radial-gradient(circle at 48% 42%, var(--glow) 0, rgba(255,255,255,0.9) 60px, rgba(143,207,207,0.5) 170px, rgba(31,138,140,0) 300px),
      linear-gradient(100deg, #2a7f77 0%, #3d9c95 35%, #1e7f7c 70%, #146a6b 100%);
  }

  .offer-title {
    position: absolute; left: 68px; top: 34px;
    font: 400 54px/1 "Share Tech Mono", monospace;
    letter-spacing: 2px;
  }
  .offer-detail {
    position: absolute; left: 68px; top: 92px;
    font: 400 17px/19px "Share Tech Mono", monospace;
    letter-spacing: 6.5px; text-transform: uppercase;
  }

  .big-offer {
    position: absolute; left: 90px; top: 552px;
    font: 400 92px/1 "Questrial", sans-serif;
    letter-spacing: 1px;
  }
  .big-offer-detail {
    position: absolute; left: 92px; top: 638px;
    font: 400 15px/1 "Share Tech Mono", monospace;
    letter-spacing: 11.4px; color: var(--ink);
  }

  .brand {
    position: absolute; left: 0; right: 0;
    text-align: center; white-space: nowrap;
    color: var(--ink);
    font: 400 24px/1 "Hind", sans-serif;
  }
  .flyer--colour .brand { top: 582px; left: -20px; }
  .flyer--cut .brand { top: 320px; left: -40px; font-size: 30px; }

  .footer {
    position: absolute; top: 694px; display: flex;
    font-family: "Hind", sans-serif;
  }
  .flyer--colour .footer { left: 92px; }
  .flyer--cut .footer { left: 94px; }
  .terms { list-style: none; width: 182px; font-size: 10.5px; line-height: 13.4px; }
  .contact {
    border-left: 1px solid var(--rule);
    padding-left: 25px; height: 52px;
    font-size: 12.5px; line-height: 16px;
  }
</style>
</head>
<body>
<main class="canvas">

  <section class="flyer flyer--colour">
    <h1 class="offer-title">1/2 HEAD FOILS</h1>
    <p class="offer-detail">Or all over colour,<br>cut and finish<br>$120</p>
    <p class="brand">Velvet Strands For Hair</p>
    <footer class="footer">
      <ul class="terms">
        <li>*toners and treatment extra costs</li>
        <li>*expires 31/03/15</li>
        <li>*butler salon only</li>
        <li>*not valid with any other offers</li>
      </ul>
      <p class="contact">9318 7061<br>Shop 3/7 Marlowe pde Butler</p>
    </footer>
  </section>

  <section class="flyer flyer--cut">
    <div class="hero-photo" role="img" aria-label="Close-up portrait of a model with a sleek, glossy teal-toned bob framing her face, lit by a soft white glow"></div>
    <p class="brand">Velvet Strands For Hair</p>
    <h1 class="big-offer">50% OFF</h1>
    <p class="big-offer-detail">STYLE CUT AND FINISH</p>
    <footer class="footer">
      <ul class="terms">
        <li>*not valid Saturdays</li>
        <li>*expires 31/03/15</li>
        <li>*butler salon only</li>
        <li>*not valid with any other offers</li>
      </ul>
      <p class="contact">9318 7061<br>Shop 3/7 Marlowe pde Butler</p>
    </footer>
  </section>

</main>
</body>
</html>
```